Business Name is RT Glamworks - Make-up Artist

I'm looking for an attractive and eye catching business card for for mobile make-up artist business. On the front of the card, I just want the name RT Glamworks in feminine type cursive writing and underneath my name Tessa Rowan and Make-Up Artist.
On the back of the card, I would like written down one side the following;
Make-Up Tutorials
Bridal
Photography
Debutante
Formals
Family Portraits
I would also like the following details as well as the Chatterly and Picvault Icons;
Mobile: 0482 615 379
Email: tessarowan@mailbrook.net
Website: tessarowan.velmira.com
Certificate III in Make-Up
Also, I would like a section that says Your Next Appointment and a space to put that information.
I would also like the Velmira Symbol on the bottom right hand corner (I have attached)

Target Market(s)

Mostly females

Industry/Entity Type

Makeup

Contact Information for Business Card

RT Glamworks
Tessa Rowan - Make-Up Artist

Font styles to use
Script

Colors
b768aa
886aae
e34297

Requirements
Must have
• Mobile: 0482 615 379
• Email: tessarowan@mailbrook.net
• Website: tessarowan.velmira.com
• Certificate III in Make-Up
Nice to have
• Something to do with make-up like a smudged lipstick or some eye shadow
Should not have
• Don't want it too busy

```html
<!DOCTYPE html>
<html lang="en">
<head>
<meta charset="utf-8">
<title>RT Glamworks – Business Cards</title>
<link rel="stylesheet" href="https://fonts.googleapis.com/css2?family=Marcellus+SC&family=Lato:wght@400&display=swap">
<style>
  :root {
    --backdrop: #ecebe9;
    --kraft-light: #cfb28a;
    --kraft-mid: #c09c71;
    --kraft-dark: #a88660;
    --ink: #141210;
    --paper: #ffffff;
    --rule: #9a9a9a;
    --mark: #4a4a4a;
  }
  * { margin: 0; padding: 0; box-sizing: border-box; }
  html, body { width: 1200px; height: 900px; overflow: hidden; }
  body { background: var(--backdrop); position: relative; color: var(--ink); }

  .card {
    position: absolute;
    overflow: hidden;
    box-shadow: 0 6px 18px rgba(0,0,0,0.18);
  }
  .kraft {
    background: linear-gradient(160deg, var(--kraft-light) 0%, var(--kraft-mid) 55%, var(--kraft-dark) 100%);
  }
  .line { position: absolute; left: 0; right: 0; text-align: center; line-height: 1; white-space: nowrap; }

  .brand-name { font-family: "Marcellus SC", serif; font-size: 40px; letter-spacing: 1px; }
  .brand-role { font-family: "Lato", sans-serif; font-size: 14.5px; letter-spacing: 1.6px; text-transform: uppercase; }
  .body-text { font-family: "Lato", sans-serif; font-size: 15.5px; }

  /* Info card */
  .card-info { left: 238px; top: 62px; width: 555px; height: 343px; }
  .card-info .brand-name { top: 45px; }
  .card-info .brand-role { top: 91px; }
  .card-info .cert { top: 116px; }
  .contact-divider { position: absolute; left: 178px; top: 154px; width: 198px; height: 20px; }
  .card-info .phone { top: 181px; }
  .card-info .email { top: 202px; }
  .card-info .web { top: 222px; }
  .contact-rule { position: absolute; left: 182px; width: 192px; top: 250px; height: 1px; background: var(--ink); }
  .card-info .services-1 { top: 266px; }
  .card-info .services-2 { top: 286px; }

  /* Appointment card */
  .card-appointment { left: 452px; top: 465px; width: 560px; height: 343px; background: var(--paper); }
  .appointment-band { position: absolute; left: 0; top: 0; width: 100%; height: 182px; }
  .card-appointment .brand-name { top: 63px; }
  .card-appointment .brand-role { top: 107px; }
  .mark-tab { position: absolute; left: 227px; top: 152px; width: 106px; height: 32px; background: var(--paper); }
  .partner-mark { position: absolute; left: 0; right: 0; top: 166px; display: flex; flex-direction: column; align-items: center; gap: 4px; }
  .partner-dot { width: 22px; height: 22px; border-radius: 50%; background: var(--mark); }
  .partner-name { font-family: "Marcellus SC", serif; font-size: 12px; color: var(--mark); letter-spacing: 1px; }
  .appointment-label { top: 250px; font-family: "Marcellus SC", serif; font-size: 21px; letter-spacing: 0.8px; }
  .appointment-rule { position: absolute; left: 108px; width: 345px; top: 319px; height: 2px; background: var(--rule); }
</style>
</head>
<body>

  <section class="card card-info kraft">
    <div class="line brand-name">RT Glamworks</div>
    <div class="line brand-role">Tessa Rowan - Make-Up Artist</div>
    <div class="line body-text cert">Certificate III in Make-Up</div>

    <svg class="contact-divider" viewBox="0 0 198 20" aria-hidden="true">
      <line x1="0" y1="10" x2="60" y2="10" stroke="#141210" stroke-width="1"/>
      <line x1="138" y1="10" x2="198" y2="10" stroke="#141210" stroke-width="1"/>
      <!-- phone -->
      <circle cx="76" cy="10" r="9" fill="#141210"/>
      <rect x="72.5" y="4" width="7" height="12" rx="1.3" fill="none" stroke="#cfb28a" stroke-width="1.3"/>
      <!-- mail -->
      <circle cx="99" cy="10" r="9" fill="#141210"/>
      <rect x="94" y="6.5" width="10" height="7" fill="none" stroke="#cfb28a" stroke-width="1.2"/>
      <polyline points="94,6.5 99,10.5 104,6.5" fill="none" stroke="#cfb28a" stroke-width="1.2"/>
      <!-- web -->
      <circle cx="122" cy="10" r="9" fill="#141210"/>
      <circle cx="122" cy="10" r="5" fill="none" stroke="#cfb28a" stroke-width="1.2"/>
      <line x1="117" y1="10" x2="127" y2="10" stroke="#cfb28a" stroke-width="1"/>
      <ellipse cx="122" cy="10" rx="2.2" ry="5" fill="none" stroke="#cfb28a" stroke-width="1"/>
    </svg>

    <div class="line body-text phone">0482 615 379</div>
    <div class="line body-text email">tessarowan@mailbrook.net</div>
    <div class="line body-text web">tessarowan.velmira.com</div>
    <div class="contact-rule"></div>
    <div class="line body-text services-1">Make-Up Tutorials | Bridal | Photography</div>
    <div class="line body-text services-2">Debutante | Formals | Family Portraits</div>
  </section>

  <section class="card card-appointment">
    <div class="appointment-band kraft"></div>
    <div class="line brand-name">RT Glamworks</div>
    <div class="line brand-role">Tessa Rowan - Make-Up Artist</div>
    <div class="mark-tab"></div>
    <div class="partner-mark">
      <span class="partner-dot"></span>
      <span class="partner-name">Velmira</span>
    </div>
    <div class="line appointment-label">Your Next Appointment</div>
    <div class="appointment-rule"></div>
  </section>

</body>
</html>
```